Bellmoor Commercial Finance Information Brochure

This brochure will be sent out to clients via A4 PDF on an email to showcase what our company has to offer. We are a commercial finance brokerage, that specialises in property finance. We would like to see designs following our colour scheme. The final design should demonstrate our professionalism and reliability.
I have attached our logo and also a few bullet points on our information and what we can offer. These can be slightly reworded for conciseness. Or leave the text sections as filler and I can fill these in.
I have also attached an overview of our colour scheme and design styling for your consideration.
Target Market(s)
Property Developers
Industry/Entity Type
Financial Services

```html
<!DOCTYPE html>
<html lang="en">
<head>
<meta charset="utf-8">
<title>Bellmoor Finance – A4 PDF Brochure</title>
<link href="https://fonts.googleapis.com/css2?family=Montserrat:wght@400;500;700&display=swap" rel="stylesheet">
<style>
  :root{
    --brand-blue:#0b4fa3;
    --brand-green:#24903f;
    --ink:#222222;
    --title-ink:#333333;
    --panel-grey:#f4f4f4;
    --paper:#ffffff;
  }
  *{margin:0;padding:0;box-sizing:border-box}
  html,body{width:1200px;height:691px;overflow:hidden;background:var(--paper)}
  body{position:relative;font-family:"Montserrat",Arial,sans-serif;color:var(--ink)}

  .brand-name{font-family:"Montserrat",Arial,sans-serif;font-weight:700;color:var(--brand-blue);
    text-align:center;letter-spacing:.06em;white-space:nowrap;position:absolute}
  .brand-name--header{top:46px;left:0;width:1200px;font-size:22px}
  .sheet-title{position:absolute;top:100px;left:0;width:1200px;text-align:center;
    font-size:33px;font-weight:700;color:var(--title-ink);letter-spacing:-.01em}

  .page{position:absolute;top:173px;width:322px;height:456px;background:var(--paper);
    overflow:hidden;box-shadow:0 1px 4px rgba(0,0,0,.18)}
  .page--cover{left:72px}
  .page--about{left:441px}
  .page--contact{left:813px}

  .photo{position:absolute;display:block}
  .cover-photo{left:0;top:92px;width:322px;height:364px;
    background:linear-gradient(160deg,#5b6266 0%,#8d9499 30%,#3d4245 60%,#1e2224 100%)}
  .cover-band{position:absolute;left:0;top:0;width:322px;height:118px}
  .brand-name--cover{top:42px;left:0;width:322px;font-size:17px;color:var(--paper)}

  .brand-name--page{top:24px;left:0;width:322px;font-size:12px}

  .copy{position:absolute;font-size:7.3px;line-height:8.5px;font-weight:400}
  .copy--center{text-align:center}

  .about-intro{left:24px;top:68px;width:274px}
  .grey-panel{position:absolute;left:0;top:129px;width:322px;height:124px;background:var(--panel-grey)}
  .about-founding{left:20px;top:153px;width:138px}
  .about-photo{left:160px;top:129px;width:162px;height:124px}
  .green-band{position:absolute;left:0;width:322px;background:var(--brand-green)}
  .about-band{top:276px;height:76px}
  .about-approach{left:24px;top:300px;width:274px;color:var(--paper)}
  .about-network{left:26px;top:373px;width:270px}

  .contact-intro{left:24px;top:68px;width:274px}
  .contact-tech{left:30px;top:113px;width:262px}
  .contact-band{top:180px;height:145px}
  .contact-process{left:20px;top:200px;width:144px;color:var(--paper)}
  .contact-photo{left:176px;top:196px;width:129px;height:148px;
    background:linear-gradient(150deg,#3a3d40 0%,#55595c 45%,#a9a39a 75%,#7d7770 100%)}

  .contact-details{position:absolute;left:16px;top:356px;padding-left:5px;
    border-left:1px solid var(--ink);font-size:7.2px;line-height:9.2px;font-style:normal}
  .contact-details p{display:flex;align-items:center;gap:3px}
  .contact-details .address{margin-bottom:3px}
  .contact-details svg{width:6px;height:6px;flex:none}
  .brand-name--footer{left:204px;top:366px;width:102px;font-size:11px;line-height:13px;white-space:normal}

  .page-footer{position:absolute;left:0;bottom:0;width:322px;height:42px}
</style>
</head>
<body>

<div class="brand-name brand-name--header">BELLMOOR FINANCE</div>
<h1 class="sheet-title">A4 PDF BROCHURE</h1>

<!-- Cover -->
<section class="page page--cover">
  <div class="photo cover-photo" role="img" aria-label="Photo of a team meeting around a table with laptops in a glass-walled office"></div>
  <svg class="cover-band" viewBox="0 0 322 118" preserveAspectRatio="none" aria-hidden="true">
    <path d="M0 0H322V98Q161 90 0 104Z" fill="#ffffff"/>
    <path d="M0 0H322V94Q161 86 0 100Z" fill="var(--brand-blue)"/>
    <path d="M0 104Q161 90 322 102V108Q161 96 0 112Z" fill="var(--brand-green)"/>
  </svg>
  <div class="brand-name brand-name--cover">BELLMOOR FINANCE</div>
</section>

<!-- About -->
<section class="page page--about">
  <div class="brand-name brand-name--page">BELLMOOR FINANCE</div>
  <p class="copy copy--center about-intro">As former lenders and developers ourselves, we intimately understand the inefficiencies that plague deals in the market today. We’ve experienced the frustration of tight time limits on deals and the exasperating feeling of brokers wasting precious time collecting information. It’s enough to drive developers and lenders insane!</p>
  <div class="grey-panel"></div>
  <p class="copy about-founding">That’s why we founded Bellmoor Finance – to be the efficient and reliable link that connects developers and lenders. We’ve streamlined our processes to eliminate unnecessary hurdles, enabling clear and swift communication between all parties involved. No more wasted time. No more unnecessary stress.</p>
  <svg class="photo about-photo" viewBox="0 0 162 124" preserveAspectRatio="none" role="img" aria-label="Photo of a smiling team gathered around a laptop in a bright office">
    <defs>
      <linearGradient id="aboutPhotoTone" x1="0" y1="0" x2="1" y2="1">
        <stop offset="0" stop-color="#e8ecef"/>
        <stop offset=".5" stop-color="#b9c0c4"/>
        <stop offset="1" stop-color="#4a4f53"/>
      </linearGradient>
    </defs>
    <path d="M12 0H162V124H6Q20 62 12 0Z" fill="url(#aboutPhotoTone)"/>
    <path d="M0 0Q14 62 4 124" fill="none" stroke="var(--brand-blue)" stroke-width="2.5"/>
  </svg>
  <div class="green-band about-band"></div>
  <p class="copy copy--center about-approach">With our expertise and industry insights, we’ve developed a unique approach that simplifies the financing journey. From the initial consultation to the final funding, we’re here to guide you every step of the way. Our goal? To make commercial financing a smooth and enjoyable experience for you.</p>
  <p class="copy copy--center about-network">With our background in the asset management industry, we have cultivated a black book of fund managers, institutions, UHNWI and private equity lenders that we can call on for non-traditional lending.</p>
  <svg class="page-footer" viewBox="0 0 322 42" preserveAspectRatio="none" aria-hidden="true">
    <path d="M14 18Q170 24 322 0V4Q170 30 14 18Z" fill="var(--brand-green)"/>
    <path d="M0 12Q170 30 322 8V42H0Z" fill="var(--brand-blue)"/>
  </svg>
</section>

<!-- Contact -->
<section class="page page--contact">
  <div class="brand-name brand-name--page">BELLMOOR FINANCE</div>
  <p class="copy copy--center contact-intro">Bellmoor Finance was created to satisfy a need in the market that has been far too overlooked. Efficiency. Efficiency is at the heart of our operations, and we pride ourselves on our ability to secure the best financing options swiftly and effectively for our clients.</p>
  <p class="copy copy--center contact-tech">By employing cutting-edge technology and streamlining our internal processes, we have cultivated a seamless and time-saving approach to finance brokering. Having been a developer, we understand the stresses and headaches associated with building, let alone all the paperwork and emails backwards and forwards between yourself and brokers to attain the necessary financing.</p>
  <div class="green-band contact-band"></div>
  <p class="copy contact-process">We are well-versed in the questions lenders will ask, allowing us to get ahead of the curve and request all the necessary information from you on day one. This approach provides you with a distinct advantage, as it eliminates the need to allocate hours each day to answering questions and fulfilling requests from brokers. By entrusting us with this responsibility, you can focus on your core tasks and leave the financing aspect to us, making the process less stressful for you.</p>
  <div class="photo contact-photo" role="img" aria-label="Photo of a smiling businessman working at a laptop in an office"></div>

  <address class="contact-details">
    <div class="address">412 Harlow Street<br>Fairview, Oregon 97024</div>
    <p><svg viewBox="0 0 10 10" aria-hidden="true"><path d="M2 1l2 2-1 1.2q1 2 2.8 2.8L7 6l2 2-1.3 1.3Q4 9 1 2.3Z" fill="var(--ink)"/></svg>555-214-7730</p>
    <p><svg viewBox="0 0 10 10" aria-hidden="true"><rect x="3" y="0.5" width="4.5" height="9" rx="0.8" fill="none" stroke="var(--ink)" stroke-width="1.2"/></svg>555-308-9162</p>
    <p><svg viewBox="0 0 10 10" aria-hidden="true"><rect x="0.5" y="2" width="9" height="6" fill="var(--ink)"/><path d="M0.5 2L5 5.5L9.5 2" fill="none" stroke="#fff" stroke-width="0.8"/></svg>hello@bellmoorfinance.com</p>
    <p><svg viewBox="0 0 10 10" aria-hidden="true"><circle cx="5" cy="5" r="4.4" fill="var(--ink)"/><path d="M0.6 5H9.4M5 0.6Q2.5 5 5 9.4M5 0.6Q7.5 5 5 9.4" fill="none" stroke="#fff" stroke-width="0.6"/></svg>www.bellmoorfinance.com</p>
  </address>
  <div class="brand-name brand-name--footer">BELLMOOR FINANCE</div>

  <svg class="page-footer" viewBox="0 0 322 42" preserveAspectRatio="none" aria-hidden="true">
    <path d="M14 18Q170 24 322 0V4Q170 30 14 18Z" fill="var(--brand-green)"/>
    <path d="M0 12Q170 30 322 8V42H0Z" fill="var(--brand-blue)"/>
  </svg>
</section>

</body>
</html>
```